Salon and Spa Distributor Business Card

Need a business card. We are are distributor in the salon and spa industry. We identify with natural beauty. Need a card with:
Company Name: Petal Harbor"
Title: "President & CEO"
Address
Company Phone number
email
website
Tag Line:" The Professional Salon Source"

Industry/Entity Type

Business

Contact Information for Business Card

Name: Leo Mendoza
Title: "President & CEO"
Address: 317 Birchline Ave, Westbrook, NJ 08412
Company Phone number: 800-463-5108
email: leomendoza@petalharbor-example.com
website: www.petalharbor-example.com

Requirements
Should not have
• No black backgrounds

```html
<!DOCTYPE html>
<html lang="en">
<head>
<meta charset="utf-8">
<title>Petal Harbor Business Card</title>
<link rel="stylesheet" href="https://fonts.googleapis.com/css2?family=Didact+Gothic&display=swap">
<style>
  :root {
    --backdrop: #222222;
    --green-deep: #2a7f3a;
    --green-mid: #4ea43f;
    --green-light: #66bb46;
    --green-text: #3f8f3c;
    --ink: #1e1e1e;
    --paper: #ffffff;
  }
  * { margin: 0; padding: 0; box-sizing: border-box; }
  html, body { width: 1189px; height: 1200px; overflow: hidden; }
  body {
    background: var(--backdrop);
    font-family: "Didact Gothic", "Century Gothic", sans-serif;
    position: relative;
  }
  .card {
    position: absolute;
    left: 171px;
    width: 856px;
    height: 488px;
    border-radius: 18px;
    overflow: hidden;
    box-shadow: 0 3px 6px rgba(0,0,0,0.55);
  }
  .card-front {
    top: 67px;
    background: radial-gradient(ellipse at 52% 45%, var(--green-light) 0%, var(--green-mid) 45%, var(--green-deep) 100%);
  }
  .card-back { top: 626px; background: var(--paper); }

  .front-brand {
    position: absolute;
    left: 130px;
    top: 180px;
    display: flex;
    align-items: center;
    gap: 34px;
    color: var(--paper);
  }
  .brand-dot {
    width: 118px; height: 118px;
    border-radius: 50%;
    background: var(--paper);
    flex: none;
  }
  .front-name { font-size: 56px; line-height: 1; letter-spacing: 0.5px; }
  .front-tagline { font-size: 23px; margin-top: 14px; letter-spacing: 1.2px; }

  .back-art { position: absolute; left: 0; top: 0; width: 380px; height: 488px; }

  .back-info { position: absolute; left: 453px; top: 68px; color: var(--ink); }
  .back-name { font-size: 54px; line-height: 1; color: var(--green-text); letter-spacing: 0.3px; }
  .back-tagline { font-size: 23px; margin-top: 6px; }
  .person { margin-top: 74px; }
  .person-name { font-size: 31px; color: var(--green-text); line-height: 1.1; }
  .person-title { font-size: 23px; line-height: 1.2; }
  .address { margin-top: 24px; font-size: 23px; line-height: 1.25; }
  .contacts { margin-top: 16px; list-style: none; }
  .contacts li { display: flex; align-items: center; gap: 10px; font-size: 21px; height: 28px; }
  .contacts li.long { font-size: 19px; }
  .icon {
    width: 24px; height: 24px; flex: none;
    background: var(--green-mid);
    border-radius: 4px;
    display: flex; align-items: center; justify-content: center;
  }
</style>
</head>
<body>
  <section class="card card-front" aria-label="Business card front">
    <div class="front-brand">
      <span class="brand-dot"></span>
      <div>
        <div class="front-name">Petal Harbor</div>
        <div class="front-tagline">The Professional Salon Source</div>
      </div>
    </div>
  </section>

  <section class="card card-back" aria-label="Business card back">
    <svg class="back-art" viewBox="0 0 380 488" role="img" aria-label="Large green illustration of a woman's profile with flowing hair and leaves">
      <defs>
        <linearGradient id="artGrad" x1="0" y1="0" x2="1" y2="1">
          <stop offset="0" stop-color="#6cbf4a"/>
          <stop offset="0.6" stop-color="#58ad43"/>
          <stop offset="1" stop-color="#2f8a3c"/>
        </linearGradient>
      </defs>
      <path d="M0 0 H250 C330 60 360 180 370 330 C375 400 360 450 340 488 H0 Z" fill="url(#artGrad)"/>
    </svg>
    <div class="back-info">
      <div class="back-name">Petal Harbor</div>
      <div class="back-tagline">The Professional Salon Source</div>
      <div class="person">
        <div class="person-name">Leo Mendoza</div>
        <div class="person-title">President &amp; CEO</div>
      </div>
      <address class="address" style="font-style:normal">317 Birchline Ave,<br>Westbrook, NJ 08412</address>
      <ul class="contacts">
        <li><span class="icon"><svg width="16" height="16" viewBox="0 0 16 16"><path d="M3 2 L6 2 L7 5 L5.5 6.5 C6.5 8.5 7.5 9.5 9.5 10.5 L11 9 L14 10 L14 13 C8 14 2 8 3 2 Z" fill="#fff"/></svg></span>800-463-5108</li>
        <li class="long"><span class="icon"><svg width="16" height="12" viewBox="0 0 16 12"><rect x="1" y="1" width="14" height="10" fill="none" stroke="#fff" stroke-width="1.4"/><path d="M1 1 L8 7 L15 1" fill="none" stroke="#fff" stroke-width="1.4"/></svg></span>leomendoza@petalharbor-example.com</li>
        <li class="long"><span class="icon"><svg width="16" height="16" viewBox="0 0 16 16"><circle cx="8" cy="8" r="6.5" fill="none" stroke="#fff" stroke-width="1.2"/><ellipse cx="8" cy="8" rx="3" ry="6.5" fill="none" stroke="#fff" stroke-width="1.2"/><path d="M1.5 8 H14.5" stroke="#fff" stroke-width="1.2"/></svg></span>www.petalharbor-example.com</li>
      </ul>
    </div>
  </section>
</body>
</html>
```